Harlow Crest Holdings (Remodeling company) needs a logo and business card

We need a business card design for a new company. We "flip" upmarket houses (buy, remodel and sell) in the Austin, TX area. I'd like neutral colors (grey, white, gold black). I would like it to include a simple, clean logo. Our designs are modern and uncluttered and I would like that reflected in the business card design.

Target Market(s)

Young professionals, Families, Retirees. Our properties will sell for $750k+

Industry/Entity Type

Real Estate

Contact Information for Business Card

Harlow Crets Holdings
Mona Harlow
(979) 555 0142
Owner
Rolf Tandem
(512) 555 0176
Realtor

Logo Text

Harlow Crest Holdings

Font styles to use
Serif
Script

Requirements
Must have
• Simple, classic design
Nice to have
• Clean lines, modern look
Should not have
• Too traditionally

```html
<!DOCTYPE html>
<html lang="en">
<head>
<meta charset="utf-8">
<title>Harlow Crets Holdings – Business Card</title>
<link rel="stylesheet" href="https://fonts.googleapis.com/css2?family=Old+Standard+TT:wght@400;700&display=swap">
<style>
  :root {
    --backdrop: #1c1c1c;
    --card: #262626;
    --gold: #b8891f;
    --gold-line: #9a7318;
    --silver: #c9c9c9;
    --serif: "Old Standard TT", "Times New Roman", serif;
  }
  * { margin: 0; padding: 0; box-sizing: border-box; }
  html, body {
    width: 1200px;
    height: 903px;
    overflow: hidden;
    background: var(--backdrop);
  }
  .stage {
    position: relative;
    width: 1200px;
    height: 903px;
    display: flex;
    align-items: center;
    justify-content: center;
  }
  .business-card {
    position: relative;
    width: 900px;
    height: 514px;
    background: var(--card);
    box-shadow: 0 18px 40px rgba(0, 0, 0, 0.45);
    font-family: var(--serif);
  }
  .brand-name {
    position: absolute;
    left: 120px;
    top: 88px;
    font-family: var(--serif);
    font-weight: 400;
    font-size: 54px;
    color: var(--gold);
    letter-spacing: 1px;
    white-space: nowrap;
  }
  .brand-rule {
    position: absolute;
    left: 130px;
    top: 168px;
    width: 710px;
    height: 2px;
    background: var(--gold-line);
  }
  .contact {
    position: absolute;
    left: 420px;
    width: 300px;
    text-align: center;
  }
  .contact--owner { top: 196px; }
  .contact--realtor { top: 330px; }
  .contact__name {
    font-weight: 700;
    font-size: 30px;
    color: var(--gold);
    line-height: 1.1;
  }
  .contact__role {
    font-weight: 700;
    font-size: 21px;
    color: var(--silver);
    line-height: 1.2;
  }
  .contact__phone {
    font-weight: 400;
    font-size: 23px;
    color: var(--silver);
    line-height: 1.4;
    letter-spacing: 0.5px;
  }
</style>
</head>
<body>
  <main class="stage">
    <section class="business-card" aria-label="Business card">
      <h1 class="brand-name">Harlow Crets Holdings</h1>
      <div class="brand-rule"></div>

      <div class="contact contact--owner">
        <p class="contact__name">Mona Harlow</p>
        <p class="contact__role">Owner</p>
        <p class="contact__phone">(979) 555 0142</p>
      </div>

      <div class="contact contact--realtor">
        <p class="contact__name">Rolf Tandem</p>
        <p class="contact__role">Realtor</p>
        <p class="contact__phone">(512) 555 0176</p>
      </div>
    </section>
  </main>
</body>
</html>
```